Website for Brackley Fabrication & Construction Ltd

General Note to all.

1. Piling and gas works are separate areas of work and should not be put together.
- the marine section should really be the piling works and should have all the barges/water piles etc.
- the gas section should have the big silo looking thing

2. I would like to add in Specialist Onsite Labour and Management in the 'our services' section. The would include the Supervisors, Coded Welders, Site Fitters and Crane and Rig Crews etc.

3. I did like it how someone had use the BFC header logo as the top of the webpage with the individual tabs above and the website starting below. Please remove the VAT number and phone number from this section.

4. I also liked how one designer incorporate the orange line with spark (from the logo) as a page separator representing the welding part of the business

5. Add in a Mission Statement - To go above and beyond in to ensure our clients projects are delivered safely, ahead of schedule, in any environment for the benefit of not only our customers but also our employees and communities we work in.

6. Add in Business Objectives -BFC is on a mission to be one of the leading contractors in UK to supply All Site Labour - ranging from Site Management, fully Coded Welders, Site Fitters and Crane and Rig Crews.

7. I am happy for you to add in photos that are not ours for the thumbs nails for the our services. ie a colourful welding pics/cool tunnelling pic etc - just make sure I will not get done for copy write infringements

8. I would like a some type of 'contact us' field or 'request a consultation' section.

9. Please confirm if the webpages you create will be compatible for both desktop and mobile app and how difficult it will be to update personally once it is live.

10. You have all done very well and have thus far been very impressed with what you have produced. I gave a very vague brief as I was not entirely sure how you would go about making something with very little information. Some of the designs look very professional.

11. I'm not sure how once I choose the winning design how that then transfers over to my domain? Perhaps someone can help me with that? I will also be looking for a web hosting platform so feel free to provide this information.

After using Sketch hive for successful getting a professional logo for the company I'm giving the web design option a go.

I am looking for a professional website for the above civil construction company.

The company director has many years experience in Marine, tunnelling, conveyors, stadium construction gas and piling works including piling works for coal ports, bridges and tunnels.

The company currently provide 20+ skilled and experienced guys from all trades (supervisors, coded welders, fitters, crane drivers and crane supervisors, rigglers, slingers and piling operatives) on the Corran Flowpath project in London - London's new super sewer. Most of this work is off barges carrying cranes (upto 600T and drill rigs).

As we are looking to expand and get more subcontracts we need a web presence to say who we are and what we do.

I'll include the 2 company logos we currently use below

I have included an info doc with pics you may or may not use.

Target Market(s)

Mainly other large construction companies and potential subcontractors

Industry/Entity Type

Construction Company

Coding

Coded - Design and coding required

Font styles to use
Sans Serif

Colors
0655a3
f37122
ffffff

Requirements
Must have
• Few tabs
• Simple to use/update but still professional look
• The challenge will be making the website look professional with not much available content.
Should not have
• No residential house building

```html
<!DOCTYPE html>
<html lang="en">
<head>
<meta charset="utf-8">
<title>Brackley Fabrication &amp; Construction</title>
<link href="https://fonts.googleapis.com/css2?family=Montserrat:wght@500;600;700;800&family=Roboto:wght@400;500&display=swap" rel="stylesheet">
<style>
:root{
  --blue:#0655a3;
  --orange:#f37122;
  --white:#ffffff;
  --ink:#1b1b1b;
  --text:#555b63;
  --pale:#eef3f8;
  --band:#f4f6f9;
  --footer:#1f2b38;
  --footer-deep:#17212c;
}
*{margin:0;padding:0;box-sizing:border-box}
html,body{width:1200px;height:2532px;overflow:hidden;background:var(--white)}
body{font-family:'Roboto',sans-serif;color:var(--text);position:relative}

/* top bar */
.topbar{position:absolute;top:0;left:0;width:1200px;height:37px}
.topbar-band{position:absolute;top:0;left:330px;right:0;height:37px;background:var(--blue);clip-path:polygon(0 0,100% 0,100% 100%,16px 100%)}
.topbar-info{position:absolute;right:145px;top:0;height:37px;display:flex;gap:38px;align-items:center;color:var(--white);font-size:11px}
.topbar-info span{display:flex;align-items:center;gap:8px}
.brand{position:absolute;left:160px;top:10px;display:flex;align-items:center;gap:8px}
.brand-mark{width:22px;height:22px;border:3px solid var(--blue);border-radius:50%}
.brand-name{font-family:'Montserrat',sans-serif;font-weight:800;font-size:22px;color:var(--blue);line-height:1}
.brand-sub{font-family:'Montserrat',sans-serif;font-weight:800;font-size:9px;color:var(--blue);letter-spacing:.5px}
.nav{position:absolute;top:58px;right:160px;display:flex;gap:26px;align-items:center;font-family:'Montserrat',sans-serif;font-weight:600;font-size:11px;color:var(--ink)}
.nav .active{background:var(--orange);color:var(--white);padding:6px 14px;border-radius:12px}

/* hero */
.hero{position:absolute;top:96px;left:0;width:1200px;height:394px;background:linear-gradient(180deg,#3e4650 0%,#2c333b 55%,#3b3a36 100%)}
.hero-title{position:absolute;top:100px;width:100%;text-align:center;color:var(--white);font-family:'Montserrat',sans-serif;font-weight:700}
.hero-title h1{font-size:84px;line-height:90px;letter-spacing:2px}
.hero-title p{font-size:34px;line-height:40px;font-weight:700;margin-top:2px}
.hero-btns{position:absolute;top:250px;left:407px;display:flex;gap:22px}
.btn{height:43px;display:flex;align-items:center;justify-content:space-between;padding:0 20px 0 30px;color:var(--white);font-family:'Montserrat',sans-serif;font-weight:600;font-size:13px}
.btn-blue{background:var(--blue);width:182px}
.btn-orange{background:var(--orange);width:181px}
.hero-arrow{position:absolute;top:184px;width:30px;height:30px;background:var(--white);display:flex;align-items:center;justify-content:center;border-radius:2px}

/* work areas */
.area{position:absolute;top:543px;width:375px;height:237px;border:3px solid var(--blue);padding:44px 22px 0;text-align:center;font-size:10.5px;line-height:17px}
.area.gas{border-color:var(--orange)}
.area h2{position:absolute;top:-17px;left:50%;transform:translateX(-50%);background:var(--white);padding:0 14px;font-family:'Montserrat',sans-serif;font-weight:700;font-size:22px;line-height:30px;color:var(--blue);white-space:nowrap}
.area.gas h2{color:var(--orange)}
.area .bar{position:absolute;top:22px;left:50%;width:36px;height:3px;margin-left:-18px;background:var(--ink)}
.area p+p{margin-top:17px}
.separator-art{position:absolute;left:572px;top:565px;width:80px;height:190px;background:radial-gradient(ellipse at 50% 75%,rgba(243,113,34,.35) 0%,rgba(243,113,34,.12) 40%,rgba(243,113,34,0) 70%)}

/* services */
.services{position:absolute;top:827px;left:0;width:1200px;height:469px;background:var(--pale)}
.sec-title{position:absolute;width:100%;text-align:center;font-family:'Montserrat',sans-serif;font-weight:700;font-size:23px;color:var(--blue)}
.tabs{position:absolute;top:112px;left:160px;width:880px;height:74px;border-bottom:1px solid #d3dbe4;display:flex;justify-content:space-between;padding:0 20px}
.tab{display:flex;flex-direction:column;align-items:center;gap:8px;font-family:'Montserrat',sans-serif;font-weight:600;font-size:10px;color:#333;text-align:center;line-height:12px}
.tab.on{color:var(--orange)}
.tab-line{position:absolute;left:0;bottom:-2px;width:115px;height:3px;background:var(--orange)}
.svc-photo{position:absolute;top:223px;left:160px;width:278px;height:199px;background:linear-gradient(180deg,#9fb6cc 0%,#7d8f9f 50%,#3d4650 100%)}
.svc-text{position:absolute;top:218px;left:461px;width:577px;font-size:10.5px;line-height:19px}
.svc-text p+p{margin-top:19px}

/* our work */
.filters{position:absolute;top:1404px;left:160px;width:880px;display:flex;justify-content:center;gap:18px;font-family:'Montserrat',sans-serif;font-weight:600;font-size:11px;color:var(--ink)}
.filters .on{color:var(--orange)}
.tile{position:absolute;width:278px;height:179px}
.tile.hover{background:var(--orange);display:flex;flex-direction:column;align-items:center;justify-content:center;gap:12px;color:var(--white);font-family:'Montserrat',sans-serif;font-weight:600;font-size:11px}
.tile-ring{width:36px;height:36px;border:2px solid var(--white);border-radius:50%;display:flex;align-items:center;justify-content:center}
.see-all{position:absolute;top:1877px;left:508px;width:182px;height:43px;background:var(--orange);color:var(--white);display:flex;align-items:center;justify-content:space-between;padding:0 20px 0 33px;font-family:'Montserrat',sans-serif;font-weight:600;font-size:10px}

/* partners */
.partners{position:absolute;top:1966px;left:0;width:1200px;height:169px;background:var(--band);display:flex;justify-content:center;align-items:center;gap:62px}
.partner{display:flex;align-items:center;gap:8px;font-family:'Roboto',sans-serif;font-weight:500;font-size:18px;color:#3a4450}
.partner i{display:block;width:14px;height:14px;background:#3a4450;border-radius:50%}

/* footer */
.footer{position:absolute;top:2135px;left:0;width:1200px;height:346px;background:linear-gradient(180deg,#263444 0%,var(--footer) 100%)}
.f-col{position:absolute;top:90px;color:#d7dde4;font-size:10.5px;line-height:20px}
.f-col h3{font-family:'Montserrat',sans-serif;font-weight:700;font-size:16px;color:var(--white);margin-bottom:14px;margin-top:-4px}
.f-about{left:160px;width:230px;top:86px}
.f-about .mini{float:left;width:56px;height:46px;background:var(--white);margin:4px 12px 4px 0;display:flex;align-items:center;justify-content:center;font-family:'Montserrat',sans-serif;font-weight:800;font-size:14px;color:var(--blue)}
.f-about a{color:var(--orange);text-decoration:none}
.socials{display:flex;gap:6px;margin-top:10px}
.socials i{width:14px;height:14px;border-radius:50%;background:var(--white)}
.f-tweet{left:414px;width:205px}
.f-tweet p+p{margin-top:10px}
.f-tweet b{color:var(--white)}
.f-links{left:663px}
.f-links li{list-style:none;display:flex;align-items:center;gap:10px}
.f-contact{left:836px}
.f-contact li{list-style:none;display:flex;gap:12px;margin-bottom:6px}
.copy{position:absolute;top:2481px;left:0;width:1200px;height:51px;background:var(--footer-deep);color:#c9d0d8;font-size:10.5px;display:flex;align-items:center;justify-content:center}
</style>
</head>
<body>

<header class="topbar">
  <div class="topbar-band"></div>
  <div class="brand">
    <span class="brand-mark"></span>
    <div><div class="brand-name">BFC</div><div class="brand-sub">BRACKLEY</div></div>
  </div>
  <div class="topbar-info">
    <span><svg width="12" height="12" viewBox="0 0 24 24" fill="none" stroke="#fff" stroke-width="2"><path d="M5 3h4l2 5-3 2a12 12 0 0 0 6 6l2-3 5 2v4a2 2 0 0 1-2 2A18 18 0 0 1 3 5a2 2 0 0 1 2-2z"/></svg>+ (1800) 456 7890</span>
    <span><svg width="13" height="11" viewBox="0 0 24 18" fill="none" stroke="#fff" stroke-width="2"><rect x="1" y="1" width="22" height="16"/><path d="M1 1l11 9 11-9"/></svg>info@bfc.com</span>
    <span><svg width="12" height="12" viewBox="0 0 24 24" fill="none" stroke="#fff" stroke-width="2"><circle cx="12" cy="12" r="10"/><path d="M12 6v6l4 2"/></svg>Mon - Sat 9:00 - 19:00</span>
  </div>
</header>

<nav class="nav">
  <span class="active">HOME</span><span>SERVICES</span><span>ABOUT US</span><span>OUR WORK</span><span>CONTACT</span>
</nav>

<section class="hero" role="img" aria-label="Photo of a marine construction site with cranes and barges at dusk">
  <div class="hero-arrow" style="left:64px"><svg width="8" height="12" viewBox="0 0 8 12"><path d="M6 1L1 6l5 5" fill="none" stroke="#222" stroke-width="2"/></svg></div>
  <div class="hero-arrow" style="left:1105px"><svg width="8" height="12" viewBox="0 0 8 12"><path d="M2 1l5 5-5 5" fill="none" stroke="#222" stroke-width="2"/></svg></div>
  <div class="hero-title">
    <h1>BRACKLEY</h1>
    <p>FABRICATION &amp; CONSTRUCTIONS</p>
  </div>
  <div class="hero-btns">
    <div class="btn btn-blue">CONTACT US <svg width="20" height="14" viewBox="0 0 20 14"><rect width="20" height="14" fill="#fff"/><path d="M0 0l10 8 10-8" fill="none" stroke="#0655a3" stroke-width="2"/></svg></div>
    <div class="btn btn-orange">GET A QUOTE <svg width="15" height="19" viewBox="0 0 15 19"><path d="M0 0h10l5 5v14H0z" fill="#fff"/><path d="M3 9h9M3 12h9M3 15h6" stroke="#f37122" stroke-width="1.5"/></svg></div>
  </div>
</section>

<article class="area" style="left:160px">
  <h2>PILING WORKS</h2><span class="bar"></span>
  <p>Lorem ipsum dolor sit amet, consectetur adipiscing elit. Ut fermentum metus non gravida sollicitudin. Etiam vel dolor sollicitudin, fringilla erat sollicitudin, posuere quam. Vestibulum id euismod urna. Donec sed congue tortor. Cras enim est, efficitur ac dapibus quis, consequat vitae sapien. Duis luctus venenatis magna.</p>
  <p>Aliquam nisi libero, dapibus id metus quis, congue maximus lorem. Vivamus volutpat aliquam mi. In hac habitasse platea dictumst. Etiam ac lorem ut dolor luctus sagittis vel non felis.</p>
</article>
<div class="separator-art" role="img" aria-label="Illustration of a welding torch with a spark, used as a separator"></div>
<article class="area gas" style="left:663px">
  <h2>GAS WORKS</h2><span class="bar"></span>
  <p>Lorem ipsum dolor sit amet, consectetur adipiscing elit. Ut fermentum metus non gravida sollicitudin. Etiam vel dolor sollicitudin, fringilla erat sollicitudin, posuere quam. Vestibulum id euismod urna. Donec sed congue tortor. Cras enim est, efficitur ac dapibus quis, consequat vitae sapien. Duis luctus venenatis magna.</p>
  <p>Aliquam nisi libero, dapibus id metus quis, congue maximus lorem. Vivamus volutpat aliquam mi. In hac habitasse platea dictumst. Etiam ac lorem ut dolor luctus sagittis vel non felis.</p>
</article>

<section class="services">
  <h2 class="sec-title" style="top:46px">OUR SERVICES</h2>
  <div class="tabs">
    <span class="tab-line"></span>
    <div class="tab on"><svg width="22" height="22" viewBox="0 0 24 24" fill="none" stroke="#f37122" stroke-width="1.6"><circle cx="12" cy="7" r="4"/><path d="M4 22c0-5 3.5-8 8-8s8 3 8 8z"/></svg>SUPERVISORS</div>
    <div class="tab"><svg width="22" height="22" viewBox="0 0 24 24" fill="none" stroke="#333" stroke-width="1.6"><path d="M3 3l12 12M15 15l3 6M12 18l6-3"/></svg>CODED WELDERS</div>
    <div class="tab"><svg width="22" height="22" viewBox="0 0 24 24" fill="none" stroke="#333" stroke-width="1.6"><circle cx="8" cy="7" r="3"/><path d="M2 20c0-4 3-6 6-6s6 2 6 6z"/><rect x="15" y="10" width="7" height="7"/></svg>FITTERS</div>
    <div class="tab"><svg width="22" height="22" viewBox="0 0 24 24" fill="none" stroke="#333" stroke-width="1.6"><path d="M4 22h16M7 22l3-18 10 8M10 4v18"/></svg>CRANE DRIVERS</div>
    <div class="tab"><svg width="22" height="22" viewBox="0 0 24 24" fill="none" stroke="#333" stroke-width="1.6"><path d="M6 22V3h14M6 7h14M18 7v6M4 22h6"/></svg>CRANE SUPERVISORS</div>
    <div class="tab"><svg width="22" height="22" viewBox="0 0 24 24" fill="none" stroke="#333" stroke-width="1.6"><rect x="3" y="10" width="14" height="8"/><path d="M17 13h4v5h-4M6 18v2M14 18v2M5 10l3-5h6"/></svg>RIGGLERS</div>
    <div class="tab"><svg width="22" height="22" viewBox="0 0 24 24" fill="none" stroke="#333" stroke-width="1.6"><rect x="2" y="12" width="12" height="6"/><path d="M14 14h6l2 4h-8M4 12l6-7h6"/></svg>SLINGERS AND<br>PILING OPERATIVES</div>
  </div>
  <div class="svc-photo" role="img" aria-label="Photo of site supervisors in hi-vis gear on a barge deck"></div>
  <div class="svc-text">
    <p>Lorem ipsum dolor sit amet, consectetur adipiscing elit. Ut fermentum metus non gravida sollicitudin. Etiam vel dolor sollicitudin, fringilla erat sollicitudin, posuere quam. Vestibulum id euismod urna. Donec sed congue tortor. Cras enim est, efficitur ac dapibus quis, consequat vitae sapien.</p>
    <p>Duis luctus venenatis magna, vitae ultrices leo hendrerit nec. Aliquam nisi libero, dapibus id metus quis, congue maximus lorem. Vivamus volutpat aliquam mi. In hac habitasse platea dictumst. Etiam ac lorem ut dolor luctus sagittis vel non felis. Nunc sit amet lobortis eros. Vestibulum semper tristique nulla, ut maximus nunc vehicula at.</p>
    <p>Pellentesque tincidunt venenatis magna. Sed imperdiet ultrices est ut blandit. Nunc a mauris non elit commodo elementum. Etiam sit amet erat a nulla consequat ullamcorper mollis ac nibh.</p>
  </div>
</section>

<h2 class="sec-title" style="top:1333px">OUR WORK</h2>
<div class="filters">
  <span class="on">ALL PROJECTS</span><span>BUILDINGS</span><span>MARINE</span><span>TUNNELLING</span><span>CONVEYORS</span><span>STADIUM CONSTRUCTION GAS</span><span>PILING WORKS</span><span>BRIDGES AND TUNNELS</span>
</div>
<div class="tile hover" style="left:160px;top:1448px">
  <span class="tile-ring"><svg width="16" height="16" viewBox="0 0 24 24" fill="none" stroke="#fff" stroke-width="2.2"><path d="M10 14l4-4M8 12l-3 3a3 3 0 0 0 4 4l3-3M16 12l3-3a3 3 0 0 0-4-4l-3 3"/></svg></span>
  TUNNELING
</div>
<div class="tile" style="left:461px;top:1448px;background:linear-gradient(180deg,#c9d2dc 0%,#9aa3a8 55%,#5e6b70 100%)" role="img" aria-label="Photo of a piling barge on a river with tower blocks behind"></div>
<div class="tile" style="left:761px;top:1448px;background:linear-gradient(160deg,#8c8278 0%,#b0643a 50%,#5a4a40 100%)" role="img" aria-label="Photo of workers in orange overalls on a boat"></div>
<div class="tile" style="left:160px;top:1649px;background:linear-gradient(180deg,#b8b2a4 0%,#6e6f6e 55%,#2c3136 100%)" role="img" aria-label="Photo of cranes on the river at sunset"></div>
<div class="tile" style="left:461px;top:1649px;background:linear-gradient(180deg,#8fa6c2 0%,#a67b78 50%,#6d4e4a 100%)" role="img" aria-label="Photo of a large red crawler crane on site"></div>
<div class="tile" style="left:761px;top:1649px;background:linear-gradient(160deg,#5a3438 0%,#b04a5a 45%,#d98fc4 70%,#4a3a3c 100%)" role="img" aria-label="Photo of a welder at work with bright sparks"></div>
<div class="see-all">SEE ALL WORKS <svg width="8" height="12" viewBox="0 0 8 12"><path d="M2 1l5 5-5 5" fill="none" stroke="#fff" stroke-width="2"/></svg></div>

<section class="partners">
  <span class="partner"><i></i>Corran Flowpath</span>
  <span class="partner"><i></i>Vexa</span>
  <span class="partner"><i></i>Norbridge</span>
  <span class="partner"><i></i>Harrow Civils</span>
  <span class="partner"><i></i>Keldmarine</span>
  <span class="partner"><i></i>Ostrabore</span>
</section>

<footer class="footer" role="img" aria-label="Faint photo of a riverside construction site behind the footer">
  <div class="f-col f-about">
    <span class="mini">BFC</span>
    Martin Brackley was born and raised in South East London. After finishing school he completed a Welding and Fabrication apprenticeship with Kestrel Welders and Harrow Civils. During this time <a>Read More</a>
    <div class="socials"><i></i><i></i><i></i><i></i></div>
  </div>
  <div class="f-col f-tweet">
    <h3>TWITTER FEED</h3>
    <p><b>@Lorem ipsum:</b> dolor sit amet, consectetur adipiscing elit. Ut fermentum metus non gravida sollicitudin.</p>
    <p><b>@Lorem ipsum:</b> dolor sit amet, consectetur adipiscing elit. Ut fermentum metus non gravida sollicitudin.</p>
  </div>
  <div class="f-col f-links">
    <h3>QUICK LINKS</h3>
    <ul>
      <li><svg width="10" height="8" viewBox="0 0 10 8"><path d="M0 4h9M6 1l3 3-3 3" fill="none" stroke="#fff" stroke-width="1.3"/></svg>Supervisors</li>
      <li><svg width="10" height="8" viewBox="0 0 10 8"><path d="M0 4h9M6 1l3 3-3 3" fill="none" stroke="#fff" stroke-width="1.3"/></svg>Coded Welders</li>
      <li><svg width="10" height="8" viewBox="0 0 10 8"><path d="M0 4h9M6 1l3 3-3 3" fill="none" stroke="#fff" stroke-width="1.3"/></svg>Fitters</li>
      <li><svg width="10" height="8" viewBox="0 0 10 8"><path d="M0 4h9M6 1l3 3-3 3" fill="none" stroke="#fff" stroke-width="1.3"/></svg>Crane Drivers</li>
      <li><svg width="10" height="8" viewBox="0 0 10 8"><path d="M0 4h9M6 1l3 3-3 3" fill="none" stroke="#fff" stroke-width="1.3"/></svg>Crane Supervisors</li>
      <li><svg width="10" height="8" viewBox="0 0 10 8"><path d="M0 4h9M6 1l3 3-3 3" fill="none" stroke="#fff" stroke-width="1.3"/></svg>Riggers</li>
    </ul>
  </div>
  <div class="f-col f-contact">
    <h3>GET IN TOUCH</h3>
    <ul>
      <li><svg width="12" height="10" viewBox="0 0 24 18" fill="none" stroke="#f37122" stroke-width="2"><rect x="1" y="1" width="22" height="16"/><path d="M1 1l11 9 11-9"/></svg>info@bfc.com</li>
      <li><svg width="12" height="12" viewBox="0 0 24 24" fill="none" stroke="#f37122" stroke-width="2"><path d="M5 3h4l2 5-3 2a12 12 0 0 0 6 6l2-3 5 2v4a2 2 0 0 1-2 2A18 18 0 0 1 3 5a2 2 0 0 1 2-2z"/></svg>+ (1800) 456 7890</li>
      <li><svg width="12" height="14" viewBox="0 0 24 28" fill="none" stroke="#f37122" stroke-width="2.4"><path d="M12 27s9-9 9-16a9 9 0 0 0-18 0c0 7 9 16 9 16z"/><circle cx="12" cy="11" r="3"/></svg><span>1234 Lorem Ipsum Sit,<br>Dolor Fermentum, 4567.</span></li>
    </ul>
  </div>
</footer>
<div class="copy">Copyright © 2018 Brackley fabrication &amp; construction. All rights reserved.</div>

</body>
</html>
```